Chic streamline modern edgy! Danemerecurls.com

I need a website built for my personal business. I am a hair stylist and I would like a crisp website that works well, is sleek, easy to use, and allows my clients to navigate through Services and pay deposits for services listed.

My logo is somewhat of a full moon, so my theme is nocturnal.

My information can be found at chairbook.com/danemerecurls

Target Market(s)

Women ages 25-55 who are looking for luxury hair extension services

Industry/Entity Type

Hair And Beauty

Number of Pages Required

1 page

Colors
474747
919191
d3d3d3
000000

Requirements
Must have
• Location map, coinvale link embedded for deposits, contact box, bio, faq/policies, menu of services, hours of availability by appointment only .
Nice to have
• An interactive calander where I could post dates that I am available, preferred providers for other beauty services where i could list other websites for make up and other beauty related referrals. a bridal tab would be nice to offer information about bridal services and policies.

```html
<!DOCTYPE html>
<html lang="en">
<head>
<meta charset="utf-8">
<title>Meet Dane Mere</title>
<link href="https://fonts.googleapis.com/css2?family=Roboto:wght@300;400;500;700&display=swap" rel="stylesheet">
<style>
:root{
  --night:#000000;
  --slate:#474747;
  --cell:#333333;
  --cell-dark:#1c1c1c;
  --head:#666666;
  --mist:#919191;
  --silver:#d3d3d3;
  --ink:#000000;
  --copy:#9a9a9a;
}
*{margin:0;padding:0;box-sizing:border-box}
html,body{width:1093px;height:1200px;overflow:hidden;background:var(--night)}
body{font-family:"Roboto",Arial,sans-serif}
a{text-decoration:none}
.page{position:relative;width:1093px;height:1200px}
.bio{position:absolute;left:0;top:0;width:1093px;height:600px;background:var(--night)}
.section-title{position:absolute;left:0;width:1093px;text-align:center;font-weight:400;letter-spacing:1px}
.bio .section-title{top:22px;font-size:50px;color:#4e4e4e}
.title-rule{position:absolute;left:325px;width:445px;height:1px;background:linear-gradient(90deg,transparent,#8a8a8a 50%,transparent)}
.bio .title-rule{top:84px}
.portrait{position:absolute;left:78px;top:136px;width:454px;height:464px;background:radial-gradient(ellipse at 50% 40%,#8a8a8a 0%,#5a5a5a 45%,#1a1a1a 100%);border-radius:40% 40% 0 0 / 30% 30% 0 0}
.bio-copy{position:absolute;left:558px;top:124px;width:456px}
.bio-text{font-size:13.6px;font-weight:300;line-height:28.8px;color:var(--copy);text-align:justify}
.read-more{display:inline-block;margin-top:10px;font-size:14.4px;color:var(--silver);text-decoration:underline;font-weight:300}
.pill{position:absolute;border:1.5px solid #e6e6e6;border-radius:40px;background:linear-gradient(180deg,#d6d6d6 0%,#9e9e9e 45%,#5a5a5a 100%);color:#fff;text-shadow:0 1px 2px rgba(0,0,0,.6);display:flex;align-items:center;text-decoration:none}
.pill-icon{border-radius:50%;background:#2a2a2a;border:1.5px solid #bbb;display:flex;align-items:center;justify-content:center;flex:none}
.book-now{left:558px;top:504px;width:200px;height:48px}
.book-now .pill-icon{width:32px;height:32px;margin-left:7px}
.book-now .pill-label{margin-left:30px;font-size:19px;font-weight:400}
.availability{position:absolute;left:0;top:600px;width:1093px;height:600px;background:var(--slate)}
.availability .section-title{top:38px;font-size:50px;color:var(--ink)}
.availability .title-rule{top:99px}
.panel-head{height:49px;background:var(--head);border-bottom:1px solid #888;display:flex;align-items:center;justify-content:center;font-size:24px;font-weight:500;color:var(--ink);letter-spacing:.5px}
.calendar{position:absolute;left:78px;top:171px;width:456px;border:1px solid #9a9a9a}
.calendar table{width:100%;border-collapse:collapse;table-layout:fixed}
.calendar th{height:49px;background:#222;color:#a8a8a8;font-size:14.5px;font-weight:500;border-right:1px solid #555}
.calendar td{height:48.8px;background:var(--cell);border:1px solid #555;vertical-align:top;text-align:right;padding:6px 8px 0 0;color:#a8a8a8;font-size:12px}
.calendar th:last-child,.calendar td:last-child{border-right:none}
.calendar td:first-child{border-left:none}
.calendar tr:last-child td{border-bottom:none}
.calendar td.is-marked{background:var(--cell-dark);color:#ccc}
.hours{position:absolute;left:558px;top:171px;width:456px;height:244px;border:1px solid #9a9a9a;background:var(--cell)}
.hours-list{padding:20px 0 0 100px}
.hours-row{display:flex;height:32px;align-items:center;font-size:14.5px;color:#ccc}
.hours-day{width:107px;font-weight:500}
.hours-sep{width:33px}
.hours-time{font-weight:400}
.book-appointment{left:558px;top:440px;width:456px;height:71px}
.book-appointment .pill-icon{width:48px;height:48px;margin-left:11px;background:#333;font-size:9px;font-weight:500;color:var(--silver);text-shadow:none}
.book-appointment .pill-label{margin-left:22px;font-size:29px;font-weight:400;letter-spacing:.5px}
</style>
</head>
<body>
<div class="page">
  <section class="bio">
    <h1 class="section-title">MEET DANE MERE</h1>
    <div class="title-rule"></div>
    <div class="portrait" role="img" aria-label="Black and white portrait of the stylist in a camouflage shirt"></div>
    <div class="bio-copy">
      <p class="bio-text">Professional Hair Stylist, Dane Mere, has devolved a signature approach to Hair Design. Dane studied the science of beautiful hair at Laurel Crest Academy in his native city of Dallas Texas. He continues to sharpen his skill set with continued color and cutting education from Vireo Salon Institute, Hartwell Pro, and Lumen Color. His love for healthy hair care is emphasized by his ability to create undetectable extensions. These additions not only accentuate his clients appearance, they promote growth and protection of their natural mane. To further his artistic technique, Dane travels to international hair shows and and events in the states and abroad.</p>
      <a class="read-more" href="#">» Read More</a>
    </div>
    <a class="pill book-now" href="#">
      <span class="pill-icon"><svg width="16" height="16" viewBox="0 0 16 16" fill="none" stroke="#fff" stroke-width="1.6"><path d="M3 3l5 5-5 5M8 3l5 5-5 5"/></svg></span>
      <span class="pill-label">BOOK NOW</span>
    </a>
  </section>
  <section class="availability">
    <h2 class="section-title">AVAILABILITY</h2>
    <div class="title-rule"></div>
    <div class="calendar">
      <div class="panel-head">MARCH 2016</div>
      <table>
        <tr><th>MON</th><th>TUE</th><th>WED</th><th>THU</th><th>FRI</th><th>SAT</th><th>SUN</th></tr>
        <tr><td></td><td>1</td><td>2</td><td>3</td><td>4</td><td>5</td><td>6</td></tr>
        <tr><td>7</td><td>8</td><td>9</td><td>10</td><td>11</td><td>12</td><td>13</td></tr>
        <tr><td>14</td><td>15</td><td>16</td><td>17</td><td>18</td><td>19</td><td>20</td></tr>
        <tr><td>21</td><td>22</td><td>23</td><td>24</td><td>25</td><td class="is-marked">26</td><td>27</td></tr>
        <tr><td>28</td><td>29</td><td>30</td><td></td><td></td><td></td><td></td></tr>
      </table>
    </div>
    <div class="hours">
      <div class="panel-head">BUSINESS HOURS</div>
      <div class="hours-list">
        <div class="hours-row"><span class="hours-day">Tuesday</span><span class="hours-sep">:</span><span class="hours-time">7:00am &nbsp;-&nbsp; 7:00pm</span></div>
        <div class="hours-row"><span class="hours-day">Wednesday</span><span class="hours-sep">:</span><span class="hours-time">7:00am &nbsp;-&nbsp; 7:00pm</span></div>
        <div class="hours-row"><span class="hours-day">Thursday</span><span class="hours-sep">:</span><span class="hours-time">7:00am &nbsp;-&nbsp; 7:00pm</span></div>
        <div class="hours-row"><span class="hours-day">Friday</span><span class="hours-sep">:</span><span class="hours-time">7:00am &nbsp;-&nbsp; 7:00pm</span></div>
        <div class="hours-row"><span class="hours-day">Saturday</span><span class="hours-sep">:</span><span class="hours-time">7:00am &nbsp;-&nbsp; 7:00pm</span></div>
      </div>
    </div>
    <a class="pill book-appointment" href="#">
      <span class="pill-icon">coinvale</span>
      <span class="pill-label">BOOK AN APPOINTMENT</span>
    </a>
  </section>
</div>
</body>
</html>
```